Strength Coach Business Card Design Project

I would like a business card design to complement my new logo. I would like the card to be clean, seek and strong!

Target Market(s)

Mostly adults and junior atheletes who are serious about changing their lives.

Industry/Entity Type

Business

Font styles to use
Serif

Colors

Designer to choose colors to be used in the design.

```html
<!DOCTYPE html>
<html lang="en">
<head>
<meta charset="utf-8">
<title>Vale Strength – Business Card</title>
<link rel="stylesheet" href="https://fonts.googleapis.com/css2?family=Exo+2:wght@400;500;600&display=swap">
<style>
  :root {
    --backdrop: #2a2a2c;
    --card-top: #1c1c1e;
    --card-bottom: #0d0d0e;
    --red: #e3262b;
    --red-dark: #b3161b;
    --white: #f2f2f2;
    --silver-light: #f4f4f4;
    --silver-dark: #7c7c80;
    --font-main: "Exo 2", sans-serif;
  }
  * { box-sizing: border-box; margin: 0; padding: 0; }
  html, body {
    width: 1200px;
    height: 800px;
    overflow: hidden;
    background: var(--backdrop);
    font-family: var(--font-main);
  }
  .stage {
    width: 1200px;
    height: 800px;
    display: flex;
    align-items: center;
    justify-content: center;
  }
  .business-card {
    position: relative;
    width: 840px;
    height: 480px;
    background: radial-gradient(ellipse at 30% 20%, var(--card-top), var(--card-bottom) 75%);
    box-shadow: 0 20px 50px rgba(0,0,0,0.55);
    overflow: hidden;
  }
  .brand {
    position: absolute;
    left: 70px;
    top: 70px;
    display: flex;
    align-items: center;
    gap: 26px;
  }
  .brand-mark {
    width: 96px;
    height: 96px;
    background: linear-gradient(135deg, var(--silver-light), var(--silver-dark));
  }
  .brand-divider {
    width: 3px;
    height: 110px;
    background: var(--red-dark);
  }
  .brand-name {
    font-weight: 600;
    font-size: 58px;
    letter-spacing: 3px;
    text-transform: uppercase;
    color: var(--white);
    line-height: 1;
  }
  .silver-rule {
    position: absolute;
    left: 0;
    right: 0;
    top: 236px;
    height: 5px;
    background: linear-gradient(90deg, var(--silver-dark), var(--silver-light) 45%, var(--silver-dark));
  }
  .contact-block {
    position: absolute;
    left: 70px;
    top: 272px;
  }
  .person-name {
    font-size: 34px;
    font-weight: 500;
    color: var(--red);
    letter-spacing: 1px;
    line-height: 1.1;
  }
  .person-role {
    font-size: 22px;
    color: var(--white);
    letter-spacing: 0.5px;
    margin-bottom: 14px;
  }
  .contact-list {
    list-style: none;
  }
  .contact-item {
    display: flex;
    align-items: center;
    gap: 12px;
    font-size: 29px;
    color: var(--white);
    line-height: 1.32;
    letter-spacing: 0.5px;
  }
  .contact-icon {
    width: 22px;
    height: 22px;
    flex: none;
  }
</style>
</head>
<body>
<main class="stage">
  <section class="business-card">
    <header class="brand">
      <div class="brand-mark"></div>
      <div class="brand-divider"></div>
      <div class="brand-name">Vale Strength</div>
    </header>

    <div class="silver-rule"></div>

    <div class="contact-block">
      <h1 class="person-name">Marcus Vale</h1>
      <p class="person-role">Strength and Fitness Coach</p>
      <ul class="contact-list">
        <li class="contact-item">
          <svg class="contact-icon" viewBox="0 0 24 24" aria-hidden="true">
            <path fill="#e3262b" d="M6.6 10.8a15 15 0 0 0 6.6 6.6l2.2-2.2a1 1 0 0 1 1-.25 11.4 11.4 0 0 0 3.6.57 1 1 0 0 1 1 1V20a1 1 0 0 1-1 1A17 17 0 0 1 3 4a1 1 0 0 1 1-1h3.5a1 1 0 0 1 1 1c0 1.25.2 2.45.57 3.6a1 1 0 0 1-.25 1z"/>
          </svg>
          0400 318 572
        </li>
        <li class="contact-item">
          <svg class="contact-icon" viewBox="0 0 24 24" aria-hidden="true">
            <g fill="none" stroke="#e3262b" stroke-width="2">
              <circle cx="12" cy="12" r="9.5"/>
              <ellipse cx="12" cy="12" rx="4" ry="9.5"/>
              <line x1="2.5" y1="12" x2="21.5" y2="12"/>
              <line x1="4" y1="7" x2="20" y2="7"/>
              <line x1="4" y1="17" x2="20" y2="17"/>
            </g>
          </svg>
          www.marcus-vale.co
        </li>
        <li class="contact-item">
          <svg class="contact-icon" viewBox="0 0 24 24" aria-hidden="true">
            <rect x="2" y="5" width="20" height="14" rx="1.5" fill="#e3262b"/>
            <path d="M3 6.5l9 7 9-7" fill="none" stroke="#0d0d0e" stroke-width="1.6"/>
          </svg>
          Coach@marcus-vale.co
        </li>
      </ul>
    </div>
  </section>
</main>
</body>
</html>
```